DEAN COLLOPY PROPERTY SERVICES

I want a business card that is clean and simple.
'Dean Collopy Property Services' is the title.
Somewhere on the card needs to be 'Carpentry, Tiling, painting and garden services'

On the back of card
PH 087 394 1526
email: deancollopypropertyservices@bluefinchmail.net

I have attached a picture of my other business. I would like the font and design to be similar to the bathroom business.

Many thanks.

```html
<!DOCTYPE html>
<html lang="en">
<head>
<meta charset="utf-8">
<title>Dean Collopy Property Services – Business Card</title>
<link href="https://fonts.googleapis.com/css2?family=Montserrat:wght@400;500;700&display=swap" rel="stylesheet">
<style>
  :root {
    --backdrop: #e9e9e9;
    --card: #2d2d30;
    --ink-light: #ffffff;
    --ink-soft: #e6e6e6;
    --ink-deep: #1e1e20;
  }
  * { margin: 0; padding: 0; box-sizing: border-box; }
  html, body { width: 1200px; height: 801px; overflow: hidden; }
  body {
    background: var(--backdrop);
    font-family: "Montserrat", sans-serif;
    position: relative;
  }
  .card {
    position: absolute;
    top: 245px;
    width: 530px;
    height: 310px;
    background: var(--card);
    border-radius: 4px;
    color: var(--ink-light);
    overflow: hidden;
  }
  .card--front { left: 50px; }
  .card--back { left: 620px; }

  .wordmark {
    position: absolute;
    font-size: 44px;
    font-weight: 500;
    letter-spacing: 0.5px;
    line-height: 1;
    white-space: nowrap;
  }
  .card--front .wordmark { left: 40px; top: 52px; color: var(--ink-light); }
  .card--back .wordmark { left: 0; right: 0; top: 82px; text-align: center; color: var(--ink-deep); }

  .person { position: absolute; left: 40px; top: 150px; }
  .person__name { font-size: 20px; font-weight: 700; letter-spacing: 0.5px; }
  .person__role { font-size: 15px; color: var(--ink-soft); margin-top: 2px; }

  .contact { position: absolute; left: 40px; top: 222px; list-style: none; }
  .contact__item {
    display: flex; align-items: center; gap: 8px;
    font-size: 15px; color: var(--ink-soft); line-height: 24px;
    white-space: nowrap;
  }
  .contact__icon { width: 14px; height: 14px; fill: var(--ink-light); flex: none; }
  .contact__icon--mail { fill: none; stroke: var(--ink-light); stroke-width: 2; }

  .services { position: absolute; left: 0; right: 0; top: 200px; text-align: center; }
  .services__title { font-size: 16px; font-weight: 700; letter-spacing: 0.3px; }
  .services__list { font-size: 13px; font-weight: 400; letter-spacing: 0.5px; margin-top: 8px; color: var(--ink-soft); }
</style>
</head>
<body>

<section class="card card--front" aria-label="Card front">
  <p class="wordmark">Dean Collopy</p>
  <div class="person">
    <p class="person__name">CONOR WHELAN</p>
    <p class="person__role">Manager</p>
  </div>
  <ul class="contact">
    <li class="contact__item">
      <svg class="contact__icon" viewBox="0 0 24 24" aria-hidden="true"><path d="M6.6 10.8a15.1 15.1 0 0 0 6.6 6.6l2.2-2.2a1 1 0 0 1 1-.25 11.4 11.4 0 0 0 3.6.57 1 1 0 0 1 1 1V20a1 1 0 0 1-1 1A17 17 0 0 1 3 4a1 1 0 0 1 1-1h3.5a1 1 0 0 1 1 1c0 1.25.2 2.45.57 3.57a1 1 0 0 1-.25 1z"/></svg>
      087 394 1526
    </li>
    <li class="contact__item">
      <svg class="contact__icon contact__icon--mail" viewBox="0 0 24 24" aria-hidden="true"><path d="M2 5h20v14H2z M2 5l10 8 10-8"/></svg>
      deancollopypropertyservices@bluefinchmail.net
    </li>
  </ul>
</section>

<section class="card card--back" aria-label="Card back">
  <p class="wordmark">Dean Collopy</p>
  <div class="services">
    <p class="services__title">DEAN COLLOPY PROPERTY SERVICES</p>
    <p class="services__list">&bull; CARPENTRY &bull; TILING &bull; PAINTING AND GARDEN SERVICES</p>
  </div>
</section>

</body>
</html>
```